Website Creation for Auto Repair Marketing Company - Torque Lane Promotions

This will be a website and logo for a digital marketing agency servicing the auto repair industry.

Focus on modern, efficient, and easy to understand navigation and flow. We want users to easily sign up for our Review Software and a Visibility Audit on the site. Most of the people on this site will be male and between 30-50 years old.

Industry/Entity Type

Auto Repair

Number of Pages Required

1 page

Colors

Designer to choose colors to be used in the design.

```html
<!DOCTYPE html>
<html lang="en">
<head>
<meta charset="utf-8">
<title>Torque Lane Promotions</title>
<link href="https://fonts.googleapis.com/css2?family=Nunito:wght@600;700;800&family=Open+Sans:ital,wght@0,400;0,600;0,700;1,400;1,600&display=swap" rel="stylesheet">
<style>
:root{
  --red:#d8202a;
  --red-dark:#a8111a;
  --navy:#1d2a5b;
  --navy-deep:#17224c;
  --ink:#2b2b2b;
  --text:#555;
  --grey-bg:#ececee;
  --grey-light:#f3f3f4;
  --white:#fff;
  --gold:#f2b01e;
}
*{margin:0;padding:0;box-sizing:border-box}
html,body{width:1200px;height:4289px;overflow:hidden}
body{font-family:"Open Sans",sans-serif;color:var(--text);background:var(--white);position:relative}
.abs{position:absolute}
h1,h2,h3{font-family:"Nunito",sans-serif;color:var(--ink)}
.btn{position:absolute;display:flex;align-items:center;gap:10px;border:2px solid var(--red);border-radius:24px;padding:0 4px 0 14px;color:var(--red);font-weight:700;font-size:13px;background:#fff;height:40px;white-space:nowrap}
.btn .arrow{width:30px;height:30px;border-radius:50%;background:var(--red);display:flex;align-items:center;justify-content:center}
.btn .arrow svg{width:16px;height:16px}

/* header */
.site-header{position:absolute;left:0;top:0;width:1200px;height:73px;background:rgba(22,34,80,.92);z-index:5}
.brand{position:absolute;left:172px;top:14px;display:flex;align-items:center;gap:10px}
.brand-mark{width:44px;height:44px;border:3px solid #fff;border-radius:50%}
.brand-name{font-family:"Nunito",sans-serif;font-weight:800;font-size:18px;line-height:20px;color:#fff;width:160px}
.main-nav{position:absolute;left:504px;top:26px;display:flex;gap:36px;font-size:12.5px;color:#fff;white-space:nowrap}
.main-nav .active{color:#ff5a5f;border-bottom:2px solid #ff5a5f;padding-bottom:4px}
.nav-signup{position:absolute;left:935px;top:22px;height:26px;background:var(--red);color:#fff;border-radius:14px;font-size:12px;display:flex;align-items:center;gap:8px;padding:0 3px 0 14px;white-space:nowrap}
.nav-signup span{width:20px;height:20px;border-radius:50%;background:#fff;display:flex;align-items:center;justify-content:center}

/* hero */
.hero{position:absolute;left:0;top:0;width:1200px;height:720px;background:linear-gradient(110deg,#5a4a44 0%,#3f3f4e 40%,#5c5458 70%,#8a7a70 100%)}
.hero-title{position:absolute;left:170px;top:278px;font-size:56px;line-height:62px;color:#fff;font-weight:800}
.hero .btn{left:172px;top:418px;height:34px;background:var(--red);color:#fff;border:none;font-weight:600;font-size:12px}
.hero .btn .arrow{background:#fff;width:24px;height:24px}
.hero-video{position:absolute;left:600px;top:243px;width:425px;height:262px;border:5px solid #f2f2f2;background:linear-gradient(135deg,#6c5b4f,#2f3038 60%,#9a7c5e)}
.play{position:absolute;border-radius:50%;background:var(--red);display:flex;align-items:center;justify-content:center}
.hero-dots{position:absolute;left:570px;top:666px;display:flex;gap:8px}
.hero-dots i{width:9px;height:9px;border-radius:50%;background:#fff}
.hero-dots i.on{background:var(--red)}
.hero-wave{position:absolute;left:0;top:660px;width:1200px;height:70px}

/* welcome */
.welcome{position:absolute;left:0;top:715px;width:1200px;height:715px;background:linear-gradient(90deg,var(--grey-bg) 0 598px,#fff 598px)}
.map-frame{position:absolute;left:140px;top:128px;width:330px;height:300px;background:#fff;box-shadow:0 2px 8px rgba(0,0,0,.12);padding:10px}
.map-frame div{width:100%;height:100%;background:linear-gradient(135deg,#e9ece6,#dfe5dc 60%,#bcd3ef)}
.photo-frame{position:absolute;left:317px;top:215px;width:340px;height:375px;background:#fff;padding:10px;box-shadow:0 2px 10px rgba(0,0,0,.15)}
.photo-frame .photo{width:100%;height:100%;background:linear-gradient(100deg,#c9ccd2,#8c97a8 55%,#3a4a66)}
.review-badge{position:absolute;left:340px;top:393px;width:147px;height:160px;border:2px solid #3a64c2;background:rgba(255,255,255,.92);display:flex;flex-direction:column;align-items:center;justify-content:center;gap:8px}
.review-badge .mark{width:70px;height:24px;border-radius:4px;background:#d7dbe3}
.review-badge .stars{color:var(--gold);font-size:16px;letter-spacing:2px}
.review-badge p{font-size:13px;color:#444}
.welcome h2{position:absolute;left:696px;top:135px;font-size:28px;line-height:34px;font-weight:800;width:340px}
.welcome .copy{position:absolute;left:696px;top:215px;width:332px;font-size:11px;line-height:20.3px;text-align:justify}
.welcome .btn{left:700px;top:487px}

/* what we do */
.services{position:absolute;left:0;top:1430px;width:1200px;height:695px;background:linear-gradient(100deg,#e5e5e7,#d9d9dc 60%,#cfcfd3);overflow:hidden}
.services .blob{position:absolute;left:860px;top:40px;width:620px;height:620px;border-radius:50%;background:radial-gradient(circle at 40% 40%,#ef2c34,#c10f18 70%)}
.services h2{position:absolute;left:170px;top:140px;font-size:28px;font-weight:800}
.services h3{position:absolute;left:172px;top:185px;width:330px;font-family:"Open Sans",sans-serif;font-size:17px;line-height:23px;color:var(--red);font-weight:600}
.services .copy{position:absolute;left:172px;top:245px;width:330px;font-size:11px;line-height:20.3px;text-align:justify}
.services .btn{left:174px;top:495px}
.svc{position:absolute;text-align:right;width:240px}
.svc h4{font-family:"Nunito",sans-serif;font-size:15px;color:var(--ink);font-weight:800;margin-bottom:8px}
.svc p{font-size:10.5px;line-height:17px}
.svc-icon{position:absolute;width:132px;height:132px;border-radius:50%;background:#fff;border:6px solid #e8e8ea;display:flex;align-items:center;justify-content:center;box-shadow:0 3px 10px rgba(0,0,0,.2)}
.svc-icon svg{width:64px;height:64px}

/* video */
.team-video{position:absolute;left:0;top:2125px;width:1200px;height:487px;background:linear-gradient(100deg,#6c5a54,#4a4a50 35%,#8d7c72 65%,#3e3a40)}

/* review software */
.review h2{position:absolute;font-size:28px;font-weight:800;white-space:nowrap}
.review .quote{position:absolute;left:172px;top:2780px;width:450px;font-size:17px;line-height:26px;color:var(--red);font-style:italic;font-weight:600}
.review .copy{position:absolute;left:172px;top:2872px;width:470px;font-size:10.5px;line-height:20.3px;font-style:italic;text-align:justify}
.review .btn{left:174px;top:3066px}
.audit-box{position:absolute;left:706px;top:2780px;width:321px;height:332px;background:linear-gradient(135deg,#3a3a3e,#1d1d22)}
.audit-card{position:absolute;left:27px;top:22px;width:267px;height:295px;background:#fff}
.audit-card .stars{position:absolute;left:48px;top:20px;font-size:13px;letter-spacing:3px;color:var(--gold)}
.audit-card .stars b{color:#aaa;font-weight:400}
.bar-row{position:absolute;left:44px;width:215px;display:flex;align-items:center;gap:12px;font-size:12px;line-height:14px;color:#555;white-space:nowrap}
.bar{flex:none;width:158px;height:7px;background:#cfcfcf;border-radius:4px;overflow:hidden}
.bar i{display:block;height:100%;background:var(--gold)}

/* blog */
.blog{position:absolute;left:0;top:3235px;width:1200px;height:603px;background:var(--grey-light)}
.blog h2{position:absolute;left:0;top:102px;width:1200px;text-align:center;font-size:28px;font-weight:800}
.post{position:absolute;top:160px;width:262px;height:320px;background:#fff;box-shadow:0 2px 6px rgba(0,0,0,.08)}
.post .thumb{height:153px}
.post .date{position:absolute;left:22px;top:170px;width:38px;height:42px;background:var(--red);color:#fff;text-align:center;font-family:"Nunito",sans-serif;line-height:1}
.post .date b{display:block;font-size:18px;padding-top:4px}
.post .date span{font-size:10px;font-weight:700}
.post h3{position:absolute;left:78px;top:168px;font-size:15px;line-height:21px;font-weight:800;width:150px}
.post p{position:absolute;left:22px;top:230px;width:222px;font-size:10.5px;line-height:17.5px}
.post a{position:absolute;left:22px;top:292px;font-size:10.5px;font-weight:700;color:var(--red);text-decoration:underline}

/* newsletter */
.newsletter{position:absolute;left:0;top:3838px;width:1200px;height:127px;background:linear-gradient(100deg,#b8101a,#e3232c 50%,#b5101a)}
.newsletter h2{position:absolute;left:252px;top:45px;color:#fff;font-family:"Open Sans",sans-serif;font-weight:400;font-size:22px;white-space:nowrap}
.email-field{position:absolute;left:495px;top:42px;width:475px;height:44px;border-radius:22px;background:#fff;font-size:12px;color:#444;padding:14px 0 0 22px}
.email-field .play{right:6px;top:6px;width:32px;height:32px}

/* footer */
.site-footer{position:absolute;left:0;top:3965px;width:1200px;height:324px;background:var(--navy-deep);color:#c6cbe0}
.f-col{position:absolute;top:60px;font-size:11px;line-height:22.5px;white-space:nowrap}
.f-col h4{font-family:"Open Sans",sans-serif;color:#fff;font-size:13.5px;font-weight:700;margin-bottom:12px}
.contact-item{display:flex;gap:14px;margin-bottom:10px;line-height:19px}
.contact-item svg{width:20px;height:20px;flex:none;margin-top:4px}
.copyright{position:absolute;left:180px;top:285px;font-size:10.5px}
.socials{position:absolute;left:888px;top:282px;display:flex;gap:14px}
.socials i{width:14px;height:14px;border-radius:50%;background:#fff}
.socials i:first-child{background:var(--red)}
</style>
</head>
<body>

<section class="hero">
  <div class="abs" role="img" aria-label="Photo of a marketing team working together at laptops" style="inset:0"></div>
  <h1 class="hero-title">Torque Lane<br>Promotions</h1>
  <a class="btn">Read More <span class="arrow"><svg viewBox="0 0 16 16"><path d="M3 8h9M8 4l4 4-4 4" stroke="#d8202a" stroke-width="2" fill="none"/></svg></span></a>
  <div class="hero-video" role="img" aria-label="Video still of a mechanic working under a car bonnet">
    <div class="play" style="left:183px;top:102px;width:48px;height:48px"><svg width="18" height="18" viewBox="0 0 18 18"><path d="M5 3l10 6-10 6z" fill="#fff"/></svg></div>
  </div>
  <div class="hero-dots"><i></i><i class="on"></i><i></i><i></i></div>
  <svg class="hero-wave" viewBox="0 0 1200 70" preserveAspectRatio="none">
    <path d="M0 30 C300 -10 700 70 1200 40 L1200 70 L0 70Z" fill="#fff"/>
    <path d="M0 40 C250 10 500 22 700 30 C900 38 1050 30 1200 38 L1200 48 C1050 42 900 50 700 44 C450 36 250 30 0 55Z" fill="#d8202a"/>
  </svg>
</section>

<header class="site-header">
  <div class="brand"><span class="brand-mark"></span><span class="brand-name">Torque Lane Promotions</span></div>
  <nav class="main-nav"><span class="active">Home</span><span>About Us</span><span>Software</span><span>What We Do</span><span>News</span></nav>
  <a class="nav-signup">Sign Up <span><svg width="12" height="12" viewBox="0 0 16 16"><path d="M3 8h9M8 4l4 4-4 4" stroke="#d8202a" stroke-width="2" fill="none"/></svg></span></a>
</header>

<section class="welcome">
  <div class="map-frame"><div role="img" aria-label="Street map showing local auto repair shop locations"></div></div>
  <div class="photo-frame"><div class="photo" role="img" aria-label="Portrait photo of a smiling mechanic in a workshop"></div></div>
  <div class="review-badge"><span class="mark"></span><span class="stars">★★★★★</span><p>2, 250 Reviews</p></div>
  <h2>Welcome to Torque Lane Promotions.</h2>
  <p class="copy">At vero eos et accusamus et iusto odio dignissimos ducimus qui blanditiis praesentium voluptatum deleniti atque corrupti quos dolores et quas molestias excepturi sint occaecati cupiditate non provident, similique sunt in culpa qui officia deserunt mollitia animi, id est laborum et dolorum fuga. Et harum quidem rerum facilis est et expedita distinctio. Nam libero tempore, cum soluta nobis est eligendi optio cumque vero eos et accusamus et iusto odio dignissimos ducimus qui blanditiis praesentium voluptatum deleniti atque corrupti quos dolores et quas molestias excepturi sint occaecati cupiditate non provident, similique sunt in culpa qui officia deserunt mollitia animi, id est laborum et dolorum fuga. Et harum quidem rerum facilis est et expedita distinctio.</p>
  <a class="btn">Read More <span class="arrow"><svg viewBox="0 0 16 16"><path d="M3 8h9M8 4l4 4-4 4" stroke="#fff" stroke-width="2" fill="none"/></svg></span></a>
</section>

<section class="services">
  <div class="abs" role="img" aria-label="Faded photo of a laptop and red car in the background" style="inset:0"></div>
  <div class="blob"></div>
  <h2>What We Do</h2>
  <h3>At vero eos et accusamus et idio dignissimos ducimus qui blanditiis</h3>
  <p class="copy">At vero eos et accusamus et iusto odio dignissimos ducimus qui blanditiis praesentium voluptatum deleniti atque corrupti quos dolores et quas molestias excepturi sint occaecati cupiditate non provident, similique sunt in culpa qui officia deserunt mollitia animi, id est laborum et dolorum fuga. Et harum quidem rerum facilis est et expedita distinctio. Nam libero tempore, cum soluta nobis est eligendi optio cumque vero eos et accusamus et iusto odio dignissimos ducimus qui blanditiis praesentium voluptatum deleniti atque corrupti quos dolores et quas molestias excepturi sint occaecati cupiditate non provident, similique sunt in culpa qui officia deserunt mollitia animi, id est</p>
  <a class="btn">Read More <span class="arrow"><svg viewBox="0 0 16 16"><path d="M3 8h9M8 4l4 4-4 4" stroke="#fff" stroke-width="2" fill="none"/></svg></span></a>

  <div class="svc" style="left:652px;top:115px"><h4>Lornis loresimos</h4><p>Loro eos et accusamus et iusto odio dignissimos dulorcimus qui blanditiis praesentium voluptatum</p></div>
  <div class="svc-icon" style="left:902px;top:109px"><svg viewBox="0 0 64 64" fill="none" stroke="#d8202a" stroke-width="2.5"><path d="M32 6l5 6 8-2 2 8 8 3-3 8 5 6-6 5 1 8-8 1-3 8-8-3-6 5-5-6-8 1-1-8-7-4 3-8-4-7 7-4v-8l8-1 3-7z"/><circle cx="32" cy="26" r="5"/><path d="M23 44c0-7 4-11 9-11s9 4 9 11"/></svg></div>

  <div class="svc" style="left:597px;top:280px"><h4>Lornis loresimos</h4><p>Loro eos et accusamus et iusto odio dignissimos dulorcimus qui blanditiis praesentium voluptatum</p></div>
  <div class="svc-icon" style="left:847px;top:274px"><svg viewBox="0 0 64 64" fill="none" stroke="#d8202a" stroke-width="2.5"><rect x="20" y="8" width="34" height="26" rx="3"/><path d="M8 20h8l10-6v20l-10-6H8z"/><path d="M30 16h18M30 22h18M30 28h12"/><path d="M28 58v-12l6-6 4 4 6-2v10c0 4-3 6-6 6z"/></svg></div>

  <div class="svc" style="left:652px;top:447px"><h4>Lornis loresimos</h4><p>Loro eos et accusamus et iusto odio dignissimos dulorcimus qui blanditiis praesentium voluptatum</p></div>
  <div class="svc-icon" style="left:902px;top:441px"><svg viewBox="0 0 64 64" fill="none" stroke="#d8202a" stroke-width="2.5"><path d="M12 14a9 9 0 0012 12l26 26a4 4 0 006-6L30 20a9 9 0 00-12-12l6 6-4 4z"/><path d="M52 8l4 4-10 12-6-6zM40 18L14 44l-4 10 10-4 26-26"/></svg></div>
</section>

<section class="team-video" role="img" aria-label="Video still of a team gathered around a tablet in an office">
  <div class="play" style="left:568px;top:210px;width:66px;height:66px;box-shadow:0 0 0 5px rgba(255,255,255,.3)"><svg width="22" height="22" viewBox="0 0 18 18"><path d="M5 3l10 6-10 6z" fill="#fff"/></svg></div>
</section>

<section class="review">
  <h2 style="left:170px;top:2710px">Our Review Software</h2>
  <p class="quote">“At vero eos et accusamus et idio dignissimos ducimus qui blandvero eos et accusamus et idio dignissimos ducimus qui blanditiis tiis”</p>
  <p class="copy">At vero eos et accusamus et iusto odio dignissimos ducimus qui blanditiis praesentium voluptatum deleniti atque corrupti quos dolores et quas molestias excepturi sint occaecati cupiditate non provident, similique sunt in culpa qui officia deserunt mollitia animi, id est laborum et dolorum fuga. Et harum quidem rerum facilis est et expedita distinctio. Nam libero tempore, cum soluta nobis est eligendi optio cumque vero eos et accusamus et iusto odio dignissimos ducimus qui blanditiis praesentium voluptatum deleniti atque corrupti quos dolores et quas molestias excepturi sint occaecati cupiditate non provident, similique sunt in culpa qui officia deserunt mollitia animi, id est</p>
  <a class="btn">Sign Up <span class="arrow"><svg viewBox="0 0 16 16"><path d="M3 8h9M8 4l4 4-4 4" stroke="#fff" stroke-width="2" fill="none"/></svg></span></a>

  <h2 style="left:706px;top:2710px">Visibility Audit</h2>
  <div class="audit-box">
    <div class="audit-card">
      <div class="stars">★★★★<b>★</b></div>
      <div class="bar-row" style="top:86px"><span class="bar"><i style="width:0"></i></span><span>0 User</span></div>
      <div class="bar-row" style="top:116px"><span class="bar"><i style="width:94%"></i></span><span>5 Users</span></div>
      <div class="bar-row" style="top:147px"><span class="bar"><i style="width:20%"></i></span><span>1 User</span></div>
      <div class="bar-row" style="top:177px"><span class="bar"><i style="width:72%"></i></span><span>4 Users</span></div>
      <div class="bar-row" style="top:208px"><span class="bar"><i style="width:40%"></i></span><span>2 Users</span></div>
      <div class="bar-row" style="top:238px"><span class="bar"><i style="width:58%"></i></span><span>3 Users</span></div>
    </div>
  </div>
</section>

<section class="blog">
  <h2>Latest Blog</h2>
  <article class="post" style="left:173px">
    <div class="thumb" role="img" aria-label="Photo of business people reviewing charts" style="background:linear-gradient(135deg,#c8ccd4,#6b7180)"></div>
    <div class="date"><b>01</b><span>AUG</span></div>
    <h3>Pellentesque fauc ibut accumsanultric</h3>
    <p>At vero eos et accusamus et iusto odioi gnis simos ducimus qui blanditiis praesen iulorm voluptatum deleniti atque</p>
    <a>READ MORE</a>
  </article>
  <article class="post" style="left:470px">
    <div class="thumb" role="img" aria-label="Photo of a mechanic using a diagnostic laptop in an engine bay" style="background:linear-gradient(135deg,#3b5fa8,#1e2432 60%,#5a6c90)"></div>
    <div class="date"><b>02</b><span>AUG</span></div>
    <h3>Pellentesque fauc ibut accumsanultric</h3>
    <p>At vero eos et accusamus et iusto odioi gnis simos ducimus qui blanditiis praesen iulorm voluptatum deleniti atque</p>
    <a>READ MORE</a>
  </article>
  <article class="post" style="left:767px">
    <div class="thumb" role="img" aria-label="Illustration of a digital marketing concept on a blue screen" style="background:linear-gradient(135deg,#2a3f7a,#5a8ac8 60%,#1a2652)"></div>
    <div class="date"><b>02</b><span>AUG</span></div>
    <h3>Pellentesque fauc ibut accumsanultric</h3>
    <p>At vero eos et accusamus et iusto odioi gnis simos ducimus qui blanditiis praesen iulorm voluptatum deleniti atque</p>
    <a>READ MORE</a>
  </article>
</section>

<section class="newsletter">
  <h2>Newsletter Sign up</h2>
  <div class="email-field">Email:
    <span class="play"><svg width="12" height="12" viewBox="0 0 18 18"><path d="M5 3l10 6-10 6z" fill="#fff"/></svg></span>
  </div>
</section>

<footer class="site-footer">
  <div class="f-col" style="left:182px">
    <h4>Contact</h4>
    <div class="contact-item"><svg viewBox="0 0 20 20" fill="none" stroke="#d8202a" stroke-width="1.6"><path d="M10 18s6-6 6-10a6 6 0 00-12 0c0 4 6 10 6 10z"/><circle cx="10" cy="8" r="2"/></svg><span>418 Gearwell Road,<br>Brookhaven, Ontario</span></div>
    <div class="contact-item"><svg viewBox="0 0 20 20" fill="none" stroke="#d8202a" stroke-width="1.6"><path d="M4 3l4 1 1 4-2 1a10 10 0 005 5l1-2 4 1 1 4c-8 1-15-6-14-14z"/></svg><span>555 014 2280<br>555 014 2291</span></div>
    <div class="contact-item"><svg viewBox="0 0 20 20" fill="none" stroke="#d8202a" stroke-width="1.6"><rect x="2" y="5" width="16" height="11"/><path d="M2 5l8 6 8-6"/></svg><span>hello@torquelane.test<br>owner@torquelane.test</span></div>
  </div>
  <div class="f-col" style="left:448px"><h4>About Us</h4>Lorem ipsum dolo<br>Consectetur adipiscing elit.<br>Fusce eget leo tincid<br>Donec consequat<br>Praesent elementum<br>Jmauris posueret</div>
  <div class="f-col" style="left:678px"><h4>Information</h4>Lorem ipsum dolo<br>Consectetur adipiscing elit.<br>Fusce eec consequat<br>Praesent elementum<br>Jmauris posueret<br>Aenean a ex eu lectu</div>
  <div class="f-col" style="left:891px"><h4>Other Links</h4>Lorem ipsum dolo<br>Consecteturiscing elit.<br>Fusce eget leo tincid<br>Donec consequat<br>Praesent elementum<br>Aenean a ex eu lectu</div>
  <p class="copyright">Copyright 2019 Torque Lane Promotions. All Rights Reserved</p>
  <div class="socials"><i></i><i></i><i></i><i></i><i></i></div>
</footer>

</body>
</html>
```